Vorra Fleet business card

I am needing a business card that at a glance shows all the services that we provide emphasizing some more than others. We are a Fleet and Compliance management company as well as a software company. We provide outsourced solutions for PXM compliance and HR services via our own software.
In addition, we do
drug testing
GPS
Cameras
Electronic DVIRS
ELD's

Target Market(s)

Transportation company owners

Industry/Entity Type

Transportation supplier

Contact Information for Business Card

the card should inform potential customers what we do

Other font styles liked:
• I have added brand guidelines. See attached

Requirements
Must have
• See description
Should not have
• Colors outside my brand guide. See attached

```html
<!DOCTYPE html>
<html lang="en">
<head>
<meta charset="UTF-8">
<title>Vorra Fleet – Business Card</title>
<link rel="stylesheet" href="https://fonts.googleapis.com/css2?family=Montserrat:wght@400;500;600;700&family=Roboto+Condensed:wght@400;700&display=swap">
<style>
  :root {
    --bg: #b9b9b9;
    --paper: #ffffff;
    --ink: #1a1a1a;
    --dark: #1f1e1f;
    --red: #ee2a2e;
    --muted: #4a4a4a;
    --light: #f2f2f2;
    --brand-faint: #3a393a;
  }
  * { box-sizing: border-box; margin: 0; padding: 0; }
  html, body { width: 1200px; height: 800px; overflow: hidden; }
  body {
    background: var(--bg);
    display: flex;
    flex-direction: column;
    align-items: center;
    justify-content: center;
    gap: 36px;
    font-family: "Montserrat", sans-serif;
  }
  .card {
    width: 630px;
    height: 360px;
    position: relative;
    overflow: hidden;
    box-shadow: 0 10px 24px rgba(0,0,0,.25);
  }

  /* Front */
  .card--front {
    background: var(--paper);
    border-bottom: 3px solid var(--red);
    color: var(--ink);
  }
  .brand {
    position: absolute;
    top: 48px;
    right: 52px;
    font-weight: 700;
    font-size: 40px;
    letter-spacing: 1px;
    color: var(--ink);
    text-transform: uppercase;
  }
  .holder {
    position: absolute;
    left: 52px;
    bottom: 112px;
    font-size: 24px;
    font-weight: 600;
    letter-spacing: 1.5px;
    text-transform: uppercase;
  }
  .holder__role { color: var(--red); font-weight: 500; font-size: 18px; }
  .divider {
    position: absolute;
    left: 52px;
    right: 52px;
    bottom: 92px;
    height: 1px;
    background: var(--ink);
  }
  .contacts {
    position: absolute;
    left: 52px;
    right: 52px;
    bottom: 52px;
    display: flex;
    justify-content: space-between;
    font-size: 15px;
    color: var(--muted);
    list-style: none;
  }
  .contacts li { display: flex; align-items: center; gap: 8px; white-space: nowrap; }
  .contacts svg { width: 14px; height: 14px; fill: var(--red); flex: none; }

  /* Back */
  .card--back {
    background: var(--dark);
    border-bottom: 3px solid var(--red);
    color: var(--light);
    font-family: "Roboto Condensed", sans-serif;
  }
  .brand--back {
    position: absolute;
    top: 96px;
    left: 0;
    right: 0;
    text-align: center;
    font-family: "Montserrat", sans-serif;
    font-weight: 700;
    font-size: 54px;
    letter-spacing: 2px;
    text-transform: uppercase;
    color: var(--brand-faint);
  }
  .tagline {
    position: absolute;
    left: 60px;
    right: 60px;
    top: 232px;
    display: flex;
    align-items: center;
    gap: 10px;
    color: var(--red);
    font-weight: 700;
    font-size: 20px;
    letter-spacing: .5px;
    text-transform: uppercase;
    white-space: nowrap;
  }
  .tagline::before, .tagline::after {
    content: "";
    flex: 1;
    height: 2px;
    background: var(--red);
  }
  .services {
    position: absolute;
    left: 30px;
    right: 30px;
    top: 274px;
    display: flex;
    justify-content: center;
    list-style: none;
    font-size: 15px;
    white-space: nowrap;
  }
  .services li + li::before {
    content: "|";
    margin: 0 6px;
  }
</style>
</head>
<body>

<section class="card card--front" aria-label="Business card front">
  <div class="brand">Vorra Fleet</div>
  <p class="holder">Dale Mercer <span class="holder__role">- CEO</span></p>
  <div class="divider"></div>
  <ul class="contacts">
    <li>
      <svg viewBox="0 0 24 24" aria-hidden="true"><path d="M6.6 10.8a15.1 15.1 0 0 0 6.6 6.6l2.2-2.2a1 1 0 0 1 1-.25 11.4 11.4 0 0 0 3.6.57 1 1 0 0 1 1 1V20a1 1 0 0 1-1 1A17 17 0 0 1 3 4a1 1 0 0 1 1-1h3.5a1 1 0 0 1 1 1c0 1.25.2 2.45.57 3.57a1 1 0 0 1-.25 1z"/></svg>
      (480) 555-0192
    </li>
    <li>
      <svg viewBox="0 0 24 24" aria-hidden="true"><path d="M2 5h20v14H2z M2 5l10 8 10-8" stroke="#fff" stroke-width="1.5"/></svg>
      info@vorrafleet.com
    </li>
    <li>
      <svg viewBox="0 0 24 24" aria-hidden="true"><circle cx="12" cy="12" r="10"/><path d="M2 12h20M12 2c3 3 3 17 0 20M12 2c-3 3-3 17 0 20" stroke="#fff" stroke-width="1.3" fill="none"/></svg>
      www.vorrafleet.com
    </li>
  </ul>
</section>

<section class="card card--back" aria-label="Business card back">
  <div class="brand--back">Vorra Fleet</div>
  <p class="tagline">Compliance Made Simple</p>
  <ul class="services">
    <li>Compliance</li>
    <li>Fleet Management</li>
    <li>Drug testing</li>
    <li>GPS</li>
    <li>Cameras</li>
    <li>Electronic DVIRS</li>
    <li>ELD's</li>
  </ul>
</section>

</body>
</html>
```